Remodel Flyer for realtors

"T" Ridgeline Builders

4"x 9" rack card front and back

www.BrambleworkHomes.example

555-318-4726

Let us fix what your home inspector finds!

Send us your inspection summary.

We are a licensed and Insured contractor.
CRC8071943

Serving
Marion County and Pelham Hollow

This flyer will sit in realtor offices for realtors to give to there buyers and sellers.

Target Market(s)

Realtors

Industry/Entity Type

Construction

Colors

Designer to choose colors to be used in the design.

```html
<!DOCTYPE html>
<html lang="en">
<head>
<meta charset="utf-8">
<title>"T" Ridgeline Builders – Rack Card Front and Back</title>
<link href="https://fonts.googleapis.com/css2?family=Oswald:wght@300;400;500;600&family=Roboto+Condensed:wght@400;700&display=swap" rel="stylesheet">
<style>
  :root{
    --orange:#f0921e;
    --grey:#5b5b5b;
    --grey-dark:#474747;
    --paper:#f3f3f3;
    --white:#ffffff;
    --stage:#e6e6e6;
    --ink:#3a3a3a;
  }
  *{margin:0;padding:0;box-sizing:border-box}
  html,body{width:792px;height:1200px;overflow:hidden;background:var(--stage)}
  .canvas{position:relative;width:792px;height:1200px}
  .rack-card{position:absolute;top:217px;width:340px;height:765px;background:var(--paper);
    box-shadow:0 2px 10px rgba(0,0,0,.18);overflow:hidden;font-family:'Oswald',sans-serif}
  .rack-card--front{left:37px}
  .rack-card--back{left:415px}
  .block{position:absolute}

  .brand{position:absolute;left:0;right:0;top:0;height:165px;display:flex;flex-direction:column;align-items:center;justify-content:center;gap:10px}
  .brand__square{width:58px;height:58px;background:var(--orange)}
  .brand__name{font-family:'Oswald',sans-serif;font-weight:500;color:var(--ink);text-align:center;line-height:1.15}
  .brand__name .line1{display:block;font-size:23px;letter-spacing:2px}
  .brand__name .line2{display:block;font-size:13px;letter-spacing:9px;padding-left:9px}

  .headline{left:10px;width:320px;top:165px;height:60px;background:var(--grey);color:var(--white);
    font-weight:500;font-size:21px;line-height:25px;text-align:center;display:flex;align-items:center;justify-content:center;text-transform:uppercase}
  .photo{background:linear-gradient(160deg,#e9e4da 0%,#cfc6b6 45%,#9c8a72 100%)}
  .photo--bedroom{left:10px;width:320px;top:229px;height:197px;background:linear-gradient(170deg,#f1efe9 0%,#ddd6ca 40%,#b9ab95 75%,#8f8070 100%)}
  .caption{left:10px;width:320px;top:396px;height:30px;background:rgba(255,255,255,.72);color:var(--ink);
    font-weight:300;font-size:16px;display:flex;align-items:center;justify-content:center;text-transform:uppercase}
  .serving-tab{left:10px;width:22px;top:430px;height:58px;background:var(--grey)}
  .serving{left:36px;width:294px;top:430px;height:58px;background:var(--orange);color:var(--white);
    font-weight:500;font-size:16px;line-height:23px;text-align:center;display:flex;flex-direction:column;justify-content:center;text-transform:uppercase}
  .licensed{left:10px;width:138px;top:492px;height:118px;background:var(--grey);color:var(--white);
    font-weight:300;text-align:center;display:flex;flex-direction:column;justify-content:center;text-transform:uppercase;line-height:1.2}
  .licensed .lg{font-size:19px}
  .licensed .sm{font-size:14px}
  .license-no{left:10px;width:138px;top:614px;height:42px;background:var(--orange);color:var(--white);
    font-size:20px;font-weight:400;display:flex;align-items:center;justify-content:center}
  .photo--kitchen{left:152px;width:178px;top:492px;height:164px;background:linear-gradient(180deg,#f4f2ee 0%,#cfc9c0 35%,#4a413a 70%,#2f2925 100%)}

  .contact{left:10px;width:320px;top:662px;height:90px;background:var(--grey-dark);color:var(--white);padding:8px 0 0 16px}
  .contact__row{display:flex;align-items:center;gap:10px}
  .contact__phone{font-size:40px;font-weight:400;line-height:46px}
  .contact__web{font-size:20px;font-weight:400;line-height:28px}
  .icon{flex:none}

  .photo--living{left:10px;width:320px;top:170px;height:205px;background:linear-gradient(170deg,#f3efe6 0%,#ddd2bf 40%,#c98a4a 78%,#a9642c 100%)}
  .premium{left:10px;width:148px;top:380px;height:90px;background:var(--grey);color:var(--white);text-align:center;
    display:flex;flex-direction:column;justify-content:center}
  .premium .lg{font-size:38px;font-weight:400;line-height:40px;text-transform:uppercase}
  .premium .sm{font-size:24px;font-weight:300;line-height:26px}
  .services-title{left:162px;width:168px;top:380px;height:38px;background:var(--orange);color:var(--white);
    font-size:24px;font-weight:300;display:flex;align-items:center;justify-content:center}
  .services-copy{left:162px;width:168px;top:422px;height:232px;padding:2px 4px;text-align:center;color:var(--ink);font-family:'Roboto Condensed',sans-serif}
  .services-copy h3{font-size:11.5px;font-weight:700;margin-bottom:3px}
  .services-copy p{font-size:9.2px;line-height:12.4px}
  .services-list{left:10px;width:148px;top:474px;height:180px;background:var(--orange);list-style:none;padding:16px 0 0 12px}
  .services-list li{color:var(--white);font-size:21px;font-weight:400;line-height:31px;display:flex;align-items:center;gap:10px}
  .services-list li::before{content:"";width:8px;height:8px;background:var(--white);flex:none}
</style>
</head>
<body>
<div class="canvas">

  <section class="rack-card rack-card--front" aria-label="Rack card front">
    <div class="brand">
      <div class="brand__square"></div>
      <div class="brand__name"><span class="line1">"T" RIDGELINE</span><span class="line2">BUILDERS</span></div>
    </div>
    <h1 class="block headline">Let us fix what your home<br>inspector finds!</h1>
    <div class="block photo photo--bedroom" role="img" aria-label="Photo of a bright, freshly remodeled bedroom"></div>
    <div class="block caption">Send us your inspection summary</div>
    <div class="block serving-tab"></div>
    <div class="block serving"><span>Serving</span><span>Marion County and Pelham Hollow</span></div>
    <div class="block licensed"><span class="lg">We are</span><span class="lg">a licensed and</span><span class="sm">insured contractor</span></div>
    <div class="block license-no">CRC8071943</div>
    <div class="block photo photo--kitchen" role="img" aria-label="Photo of a modern kitchen with dark cabinets and pendant lights"></div>
    <div class="block contact">
      <div class="contact__row">
        <svg class="icon" width="26" height="26" viewBox="0 0 24 24" aria-hidden="true"><path fill="#f0921e" d="M6.6 10.8a15.5 15.5 0 0 0 6.6 6.6l2.2-2.2c.3-.3.7-.4 1-.2 1.1.4 2.3.6 3.6.6.6 0 1 .4 1 1V20c0 .6-.4 1-1 1A17 17 0 0 1 3 4c0-.6.4-1 1-1h3.5c.6 0 1 .4 1 1 0 1.3.2 2.5.6 3.6.1.3 0 .7-.2 1z"/></svg>
        <span class="contact__phone">555-318-4726</span>
      </div>
      <div class="contact__row">
        <svg class="icon" width="16" height="16" viewBox="0 0 20 20" aria-hidden="true"><circle cx="10" cy="10" r="9" fill="#f0921e"/><path d="M1 10h18M10 1c3 3 3 15 0 18M10 1c-3 3-3 15 0 18" stroke="#474747" stroke-width="1.2" fill="none"/></svg>
        <span class="contact__web">www.BrambleworkHomes.example</span>
      </div>
    </div>
  </section>

  <section class="rack-card rack-card--back" aria-label="Rack card back">
    <div class="brand">
      <div class="brand__square"></div>
      <div class="brand__name"><span class="line1">"T" RIDGELINE</span><span class="line2">BUILDERS</span></div>
    </div>
    <div class="block photo photo--living" role="img" aria-label="Photo of a remodeled living room with fireplace and wood floors"></div>
    <div class="block premium"><span class="lg">Premium</span><span class="sm">Contractor</span></div>
    <h2 class="block services-title">Our Services</h2>
    <div class="block services-copy">
      <h3>Residential or Commercial</h3>
      <p>We've got all your needs covered: from residential remodels, to commercial damage repairs and everything in between. Don't hesitate to ask us a question or inquire as to why a certain process has to take place. All of our staff are friendly and knowledgeable because we know what it's like to be in your shoes. We want you to know just how special you and your project are to us, so we do our very best to ensure that you and your needs always come first. We even have a complimentary estimate where we'll come out to you!</p>
    </div>
    <ul class="block services-list">
      <li>Kitchens</li>
      <li>Bathrooms</li>
      <li>Additions</li>
      <li>Whole Homes</li>
    </ul>
    <div class="block contact">
      <div class="contact__row">
        <svg class="icon" width="26" height="26" viewBox="0 0 24 24" aria-hidden="true"><path fill="#f0921e" d="M6.6 10.8a15.5 15.5 0 0 0 6.6 6.6l2.2-2.2c.3-.3.7-.4 1-.2 1.1.4 2.3.6 3.6.6.6 0 1 .4 1 1V20c0 .6-.4 1-1 1A17 17 0 0 1 3 4c0-.6.4-1 1-1h3.5c.6 0 1 .4 1 1 0 1.3.2 2.5.6 3.6.1.3 0 .7-.2 1z"/></svg>
        <span class="contact__phone">555-318-4726</span>
      </div>
      <div class="contact__row">
        <svg class="icon" width="16" height="16" viewBox="0 0 20 20" aria-hidden="true"><circle cx="10" cy="10" r="9" fill="#f0921e"/><path d="M1 10h18M10 1c3 3 3 15 0 18M10 1c-3 3-3 15 0 18" stroke="#474747" stroke-width="1.2" fill="none"/></svg>
        <span class="contact__web">www.BrambleworkHomes.example</span>
      </div>
    </div>
  </section>

</div>
</body>
</html>
```